Electrical company 7Kites needs a new logo design.

Need business cards for electrical company.
Modern/luxury/ Smart.
Thinking Black with White text.
Attached the logo below.

We would like two versions made - each one having different contact information on (one for each company directors). Both however will have same company address -

Fennel Court 31-35 Garwick Lane
Brenmoor Isle
Eastvale Dale
SS7 4PT

Contact details 1 -
Gareth Penwright
Director
gaz@7kites-demo.co.uk
07700900318

Contact details 2 -
Kieran Ashbury
Director
07700900742
kieran@7kites-demo.co.uk

Logo Text

7 Kites Electrical Solutions

```html
<!DOCTYPE html>
<html lang="en">
<head>
<meta charset="utf-8">
<title>7Kites Business Cards</title>
<link rel="stylesheet" href="https://fonts.googleapis.com/css2?family=Montserrat:wght@300;700&display=swap">
<style>
  :root {
    --backdrop: #d4d4d2;
    --card: #060708;
    --gold: #9a7b45;
    --ink: #ffffff;
  }
  * { margin: 0; padding: 0; box-sizing: border-box; }
  html, body {
    width: 1200px; height: 900px; overflow: hidden;
    background: var(--backdrop);
    font-family: "Montserrat", sans-serif;
  }
  .canvas { position: relative; width: 1200px; height: 900px; }
  .card {
    position: absolute;
    width: 600px; height: 390px;
    background: var(--card);
    color: var(--ink);
    box-shadow: 0 6px 18px rgba(0,0,0,.25);
    overflow: hidden;
  }
  .card--front { left: 90px; top: 40px; }
  .card--back { left: 510px; top: 470px; }

  .rule {
    position: absolute; left: 0; right: 0;
    height: 2px; background: var(--gold);
  }
  .card--front .rule--top { top: 70px; }
  .card--front .rule--bottom { top: 318px; }
  .card--back .rule--bottom { top: 340px; }

  .wordmark {
    position: absolute; left: 0; right: 0; top: 166px;
    text-align: center;
    font-weight: 700;
    font-size: 44px;
    letter-spacing: 0;
    color: var(--ink);
  }

  .person { position: absolute; left: 34px; top: 118px; }
  .person__name {
    font-size: 17px; letter-spacing: 0.08em; text-transform: uppercase;
  }
  .person__first { font-weight: 300; }
  .person__last { font-weight: 700; }
  .person__role {
    margin-top: 8px;
    font-size: 11px; font-weight: 700; letter-spacing: 0.12em;
    text-transform: uppercase;
  }

  .contacts { position: absolute; left: 300px; top: 110px; list-style: none; }
  .contact {
    display: flex; align-items: flex-start; gap: 14px;
    font-size: 12px; font-weight: 700; letter-spacing: 0.06em;
    line-height: 1.35;
  }
  .contact + .contact { margin-top: 28px; }
  .contact__icon { flex: none; width: 24px; height: 24px; }
  .contact__text { padding-top: 3px; font-style: normal; }
</style>
</head>
<body>
<main class="canvas">
  <section class="card card--front" aria-label="Business card front">
    <div class="rule rule--top"></div>
    <h1 class="wordmark">7Kites</h1>
    <div class="rule rule--bottom"></div>
  </section>

  <section class="card card--back" aria-label="Business card back">
    <div class="person">
      <p class="person__name"><span class="person__first">Gareth</span> <span class="person__last">Penwright</span></p>
      <p class="person__role">Director</p>
    </div>

    <ul class="contacts">
      <li class="contact">
        <svg class="contact__icon" viewBox="0 0 24 24" aria-hidden="true">
          <circle cx="12" cy="12" r="12" fill="var(--gold)"/>
          <path d="M12 5a4.5 4.5 0 0 0-4.5 4.5C7.5 13 12 18.5 12 18.5S16.5 13 16.5 9.5A4.5 4.5 0 0 0 12 5z" fill="var(--card)"/>
          <circle cx="12" cy="9.5" r="1.6" fill="var(--gold)"/>
        </svg>
        <address class="contact__text">
          Fennel Court 31-35 Garwick Lane<br>Brenmoor Isle<br>Eastvale Dale<br>SS7 4PT
        </address>
      </li>
      <li class="contact">
        <svg class="contact__icon" viewBox="0 0 24 24" aria-hidden="true">
          <circle cx="12" cy="12" r="12" fill="var(--gold)"/>
          <rect x="8.5" y="5" width="7" height="14" rx="1.3" fill="var(--card)"/>
          <rect x="10" y="6.8" width="4" height="9" fill="var(--gold)"/>
        </svg>
        <span class="contact__text">07700900318</span>
      </li>
      <li class="contact">
        <svg class="contact__icon" viewBox="0 0 24 24" aria-hidden="true">
          <circle cx="12" cy="12" r="12" fill="var(--gold)"/>
          <rect x="6" y="8" width="12" height="8.5" rx="1" fill="var(--card)"/>
          <path d="M6.5 8.5 12 13l5.5-4.5" fill="none" stroke="var(--gold)" stroke-width="1.2"/>
        </svg>
        <span class="contact__text">gaz@7kites-demo.co.uk</span>
      </li>
    </ul>

    <div class="rule rule--bottom"></div>
  </section>
</main>
</body>
</html>
```